Country Music Cruise Design

Current site
www.rhinestonewaves.com/index.php

We want a site that is Vibrant and Colorful with cartoon style graphics. This will be a bootstrap site and shall use that idea when designing.

We want a mixture of the two sites which we really like
http://www.banjoharborvoyage.com/
and
https://drifterjam.net

Our logo is attached
Need a really nice one page design homepage with information and one page for the booking (www.rhinestonewaves.com/book)

Target Market(s)

country music fans on a cruise ship, 20-50 year old

Coding

Coded - Design and coding required

Number of Pages Required

4 page

Font styles to use
Sans Serif

Requirements
Must have
• Vibrant style colors and backgrounds like examples above.
Should not have
• Dark color

```html
<!DOCTYPE html>
<html lang="en">
<head>
<meta charset="utf-8">
<title>Rhinestone Waves Cruise</title>
<link href="https://fonts.googleapis.com/css2?family=Baloo+2:wght@700;800&family=Oswald:wght@500;600&family=Roboto+Condensed:wght@400;700&display=swap" rel="stylesheet">
<style>
:root{
  --orange:#f7941d;
  --orange-bar:#f9a825;
  --yellow:#fcc633;
  --green:#2fb65c;
  --forest:#1f3d2c;
  --hero:#5d5d5f;
  --cream:#fbf3e6;
  --ink:#222;
  --white:#fff;
}
*{margin:0;padding:0;box-sizing:border-box}
html,body{width:750px;height:1200px;overflow:hidden}
body{font-family:"Roboto Condensed",sans-serif;color:var(--ink);background:var(--white);position:relative}
.topbar{height:24px;background:var(--orange-bar);display:flex;align-items:center;padding:0 100px;font:700 8px "Roboto Condensed",sans-serif;color:var(--forest);text-transform:uppercase}
.social{display:flex;gap:3px}
.social span{width:14px;height:14px;border:1px solid var(--forest);display:block}
.topbar .contact{margin-left:14px;display:flex;gap:14px}
.topbar nav{margin-left:auto;display:flex;gap:6px}
.hero{position:relative;height:391px;overflow:hidden}
.hero-art{position:absolute;inset:0;background:linear-gradient(180deg,#6a6a6c 0%,#555 60%,#3f4f5a 85%,#2f5a6a 100%)}
.hero h4{position:absolute;top:14px;font:600 14px "Oswald",sans-serif;color:var(--white);border-bottom:2px solid var(--orange);padding-bottom:1px}
.hero .search-label{left:100px}
.hero .book-label{right:100px}
.hero .search{position:absolute;left:100px;top:50px;width:145px;border-bottom:1px solid var(--white);font-size:7px;color:var(--white);padding-bottom:2px;display:flex;justify-content:space-between}
.hero .book-link{position:absolute;right:100px;top:54px;font:700 8px "Roboto Condensed",sans-serif;color:var(--white);text-decoration:underline}
.brand{position:absolute;left:50%;top:150px;transform:translateX(-50%);display:flex;align-items:center;gap:8px;font:800 26px "Baloo 2",sans-serif;color:var(--yellow);white-space:nowrap}
.brand i{width:14px;height:14px;border-radius:50%;background:var(--yellow);display:block}
.hero-title{position:absolute;bottom:-6px;width:100%;text-align:center;font:800 44px/1 "Baloo 2",sans-serif;letter-spacing:1px;white-space:nowrap}
.hero-title .y{color:var(--yellow)}.hero-title .w{color:var(--white)}.hero-title .g{color:var(--green)}
.dates{height:218px;background:var(--green);text-align:center;padding-top:56px}
.dates h1{font:800 36px/1 "Baloo 2",sans-serif;color:var(--white)}
.dates p{font:700 8px "Roboto Condensed",sans-serif;color:var(--forest);margin:22px 0 16px;text-transform:uppercase}
.btn{display:inline-block;background:var(--forest);color:var(--white);font:700 8px "Roboto Condensed",sans-serif;text-transform:uppercase;padding:8px 23px}
.features{display:flex;height:218px}
.card{text-align:center;padding-top:27px}
.card.included{width:256px;background:var(--orange)}
.card.activities{width:237px;background:var(--yellow)}
.card.itinerary{width:257px;background:var(--forest)}
.card svg{display:block;margin:0 auto}
.card h3{font:600 18px "Oswald",sans-serif;color:var(--white);text-transform:uppercase;margin-top:8px;letter-spacing:-.3px}
.card hr{width:94px;border:0;border-top:2px solid var(--white);margin:6px auto 20px}
.card p{font:400 8px/1.3 "Roboto Condensed",sans-serif;color:var(--forest);text-transform:uppercase;height:45px;padding:0 20px}
.card.itinerary p{color:var(--white);text-transform:none;height:51px;line-height:1.25}
.card.itinerary .btn{background:var(--orange);padding:7px 19px}
.card .btn{margin-top:0}
.about{height:178px;text-align:center;padding-top:38px;background:linear-gradient(180deg,#fff,#f7f2ea)}
.about h2{font:700 18px "Baloo 2",sans-serif;color:var(--forest);letter-spacing:.3px}
.about p{font:400 8px/1.75 "Roboto Condensed",sans-serif;width:530px;margin:12px auto 0}
footer{height:142px;background:var(--cream);display:flex;padding:22px 100px 0}
.f-brand{width:168px;font-size:8px;color:var(--forest)}
.f-brand .brand-name{display:flex;align-items:center;gap:5px;font:800 14px/1.1 "Baloo 2",sans-serif;color:var(--orange);height:70px}
.f-brand .brand-name i{width:10px;height:10px;border-radius:50%;background:var(--orange);display:block;flex:none}
.f-brand div.row{margin-top:5px;display:flex;gap:4px;align-items:center}
.f-col h5{font:600 9px "Oswald",sans-serif;color:var(--forest);margin:4px 0 8px}
.f-col li{list-style:none;font-size:6.5px;line-height:12px;color:var(--forest)}
.f-col p{font-size:6.5px;color:var(--forest);line-height:1.4}
.f-info{width:99px}.f-key{width:137px}.f-news{width:146px}
.f-news .search{border-bottom:1px solid var(--forest);font-size:6.5px;padding-bottom:3px;margin-top:9px;display:flex;justify-content:space-between}
.bottombar{height:30px;display:flex;align-items:center;padding:0 100px;font:400 7px "Roboto Condensed",sans-serif;color:var(--forest)}
.bottombar nav{margin-left:54px;font-weight:700;font-size:8px}
.bottombar .social{margin-left:auto;gap:4px}
.bottombar .social span{width:18px;height:18px}
</style>
</head>
<body>
<header class="topbar">
  <div class="social"><span></span><span></span><span></span><span></span></div>
  <div class="contact">
    <span><svg width="6" height="8" viewBox="0 0 6 8"><path d="M3 0a3 3 0 0 1 3 3c0 2-3 5-3 5S0 5 0 3a3 3 0 0 1 3-3z" fill="#1f3d2c"/></svg> Lorem ipsum dolor sit</span>
    <span>|</span>
    <span>001 234 56789</span>
  </div>
  <nav><span>Prices</span>|<span>What's included?</span>|<span>FAQ's</span>|<span>Shop</span></nav>
</header>

<section class="hero">
  <div class="hero-art" role="img" aria-label="Cartoon pirate ships with black sails on either side of a treasure island and waves"></div>
  <h4 class="search-label">SEARCH</h4>
  <div class="search"><span>Search</span><svg width="8" height="8" viewBox="0 0 8 8"><circle cx="3" cy="3" r="2.3" fill="none" stroke="#fff"/><path d="M5 5l2.5 2.5" stroke="#fff"/></svg></div>
  <h4 class="book-label">BOOKING</h4>
  <span class="book-link">BOOK NOW</span>
  <div class="brand"><i></i>Rhinestone Waves Cruise</div>
  <div class="hero-title"><span class="y">RHINESTONE</span> <span class="w">WAVES</span> <span class="g">CRUISE</span></div>
</section>

<section class="dates">
  <h1>RWC 2018 - JAN 12-15TH 2018</h1>
  <p>Don't be left on shore!</p>
  <a class="btn">Book now</a>
</section>

<section class="features">
  <div class="card included">
    <svg width="36" height="36" viewBox="0 0 36 36" fill="none" stroke="#fff" stroke-width="2"><path d="M4 22h28l-4 9H8z"/><path d="M8 22v-7h20v7M12 15v-5h12v5M16 10V5h4v5"/><path d="M2 33c3 2 5 2 8 0 3 2 5 2 8 0 3 2 5 2 8 0 3 2 5 2 8 0"/></svg>
    <h3>What's included?</h3><hr>
    <p>All RWC events, food, comedy club, kids clubs, game shows, night clubs, gym, bars and water park</p>
    <a class="btn">Learn more</a>
  </div>
  <div class="card activities">
    <svg width="36" height="36" viewBox="0 0 36 36" fill="#fff"><circle cx="18" cy="8" r="3"/><path d="M15 12h6l1 10h-3l-1 10h-1l-1-10h-2z"/><circle cx="9" cy="11" r="2.5"/><circle cx="27" cy="11" r="2.5"/><path d="M6 14h6v9H6zM24 14h6v9h-6z"/></svg>
    <h3>RWC Activities</h3><hr>
    <p>We will bring on bands, Southern California's favorite DJ's, line dance lessons, two stepping, contest, offshore parties and much much more</p>
    <a class="btn">Learn more</a>
  </div>
  <div class="card itinerary">
    <svg width="36" height="36" viewBox="0 0 36 36" fill="none" stroke="#fff" stroke-width="1.5"><rect x="2" y="5" width="32" height="28"/><path d="M2 12h32"/><g fill="#fff" stroke="none"><circle cx="9" cy="18" r="1"/><circle cx="15" cy="18" r="1"/><circle cx="21" cy="18" r="1"/><circle cx="27" cy="18" r="1"/><circle cx="9" cy="25" r="1"/><circle cx="15" cy="25" r="1"/><circle cx="21" cy="25" r="1"/><circle cx="27" cy="25" r="1"/></g></svg>
    <h3>Ship itinerary</h3><hr>
    <p>January 12th -15th<br>Friday - Leave Port 5:30 PM<br>Saturday - Ensenada Mexico | Formal Dinner<br>Sunday - Day at Sea<br>Monday - 7am Return to port</p>
    <a class="btn">Learn more</a>
  </div>
</section>

<section class="about">
  <h2>RHINESTONE WAVES CRUISE</h2>
  <p>Country and Cruising? Don't miss out on this excursion that is 3 Nights – 2 Days on January 12th - 15th 2018 out of Long Beach. This cruise will be taken over by our Pacific Twang family. We are putting boots onboard for two-stepping, line dancing, multiple bands and our favorite Southern California Country DJ to bring it all together. Includes all food onboard, dance lessons, concerts, all ship activities and contest. DON'T WAIT! Rates will go up!</p>
</section>

<footer>
  <div class="f-brand">
    <div class="brand-name"><i></i>Rhinestone Waves Cruise</div>
    <div class="row"><svg width="6" height="8" viewBox="0 0 6 8"><path d="M3 0a3 3 0 0 1 3 3c0 2-3 5-3 5S0 5 0 3a3 3 0 0 1 3-3z" fill="#1f3d2c"/></svg>info@rhinestonewaves.com</div>
    <div class="row">CALL US - COMING SOON</div>
  </div>
  <div class="f-col f-info"><h5>Information</h5><ul><li>Prices</li><li>Pics &amp; Vids</li><li>Press</li><li>FAQ's</li><li>Vendors</li><li>Sponsors</li><li>About</li></ul></div>
  <div class="f-col f-key"><h5>Key Features</h5><ul><li>1. Live Bands</li><li>2. Line Dancing</li><li>3. Contest</li><li>4. All you can drink packages</li></ul></div>
  <div class="f-col f-news"><h5>Rhinestone Waves Cruise 2019</h5><p>Jan 18th - 21st 2019 (Long Holiday Weekend)</p><h5 style="margin-top:14px">Subscribe Newsletter</h5><div class="search"><span>Search</span><svg width="8" height="8" viewBox="0 0 8 8"><circle cx="3" cy="3" r="2.3" fill="none" stroke="#1f3d2c"/><path d="M5 5l2.5 2.5" stroke="#1f3d2c"/></svg></div></div>
</footer>

<div class="bottombar">
  <span>© Copyright 2018 Rhinestone Waves Cruise, All right Reserved.</span>
  <nav>Privacy Policy | Site Map | Contact Us</nav>
  <div class="social"><span></span><span></span><span></span><span></span></div>
</div>
</body>
</html>
```